Thistlewood Joinery Website

My client Thistlewood Joinery is looking for a redesign for a Word Press Website. Their current site is at www.thistlewoodjoinery.example They are a custom cabinet company, but also create bathroom, living room, bar and entertainment and bedroom cabinets too. They would like a design that emulates the master craftsman work they do yet a contemporary style.

Their current site was designed using Flash elements.

Target Market(s)

Home owners and builders of high end homes

Industry/Entity Type

Entertainment

Font styles to use
Serif
Decorative

Requirements
Must have
• Must show their work and logo using a contemporary style.
Nice to have
• Sliders that showcase their projects.

```html
<!DOCTYPE html>
<html lang="en">
<head>
<meta charset="utf-8">
<title>Thistlewood Joinery</title>
<link href="https://fonts.googleapis.com/css2?family=PT+Sans+Narrow:wght@400;700&family=Sorts+Mill+Goudy:ital@0;1&family=Mulish:ital,wght@0,400;0,600;1,400&family=Rokkitt:wght@700&display=swap" rel="stylesheet">
<style>
:root{
  --dark:#1f1f1f;
  --hero:#242424;
  --band:#6f6f75;
  --green:#3cb43c;
  --green-dark:#2e9a2e;
  --white:#ffffff;
  --text:#4a4a4a;
  --heading:#2a2a2a;
  --grey-bg:#e4e4e4;
  --icon:#5a5a5a;
}
*{margin:0;padding:0;box-sizing:border-box}
html,body{width:1066px;height:1200px;overflow:hidden;background:var(--white)}
body{position:relative;font-family:"Mulish",Arial,sans-serif}
.abs{position:absolute}

.top-bar{left:0;top:0;width:1066px;height:27px;background:var(--dark);color:var(--white);font-size:11.5px}
.top-bar span{position:absolute;top:7px}
.top-bar .divider{left:892px}

.header{left:0;top:27px;width:1066px;height:102px;background:var(--white)}
.brand{left:107px;top:30px;display:flex;align-items:center;gap:10px}
.brand-dot{width:22px;height:22px;border-radius:50%;background:var(--green)}
.brand-name{font-family:"PT Sans Narrow",Arial,sans-serif;font-weight:700;font-size:22px;color:var(--heading)}
.nav{right:101px;top:36px;display:flex;gap:20px;align-items:center;font-family:"PT Sans Narrow",Arial,sans-serif;font-size:15px;color:var(--heading)}
.nav a{color:inherit;text-decoration:none;padding:5px 0}
.nav a.active{background:var(--green);color:var(--white);padding:5px 11px;border-radius:2px;margin-right:-8px}

.hero{left:0;top:129px;width:1066px;height:478px;background:var(--hero)}
.hero-photo{left:95px;top:0}
.hero-title{left:0;top:332px;width:1066px;text-align:center;font-family:"Sorts Mill Goudy",Georgia,serif;font-style:italic;font-size:33px;color:var(--white)}
.hero-sub{left:0;top:374px;width:1066px;text-align:center;font-style:italic;font-size:12.6px;line-height:20px;color:var(--white)}
.hero-band{left:0;top:607px;width:1066px;height:7px;background:var(--band)}

.room-icon{top:565px;width:76px;height:86px}

.about-title{left:108px;top:693px;font-family:"Sorts Mill Goudy",Georgia,serif;font-style:italic;font-size:26px;color:var(--heading)}
.about-text{left:108px;top:736px;width:520px;font-size:13px;line-height:22.2px;color:var(--text)}

.video-card{left:655px;top:708px;width:302px;height:168px;background:var(--white);box-shadow:0 0 3px rgba(0,0,0,.3), 0 10px 8px -6px rgba(0,0,0,.35)}
.video-screen{left:8px;top:8px;width:286px;height:154px;background:linear-gradient(100deg,#4b4b4e,#9c9a96 45%,#cfc6b8 70%,#7a6d60)}
.video-controls{left:0;bottom:0;width:286px;height:17px;background:#111}
.video-progress{left:0;top:-3px;width:286px;height:3px;background:#555}
.video-progress i{display:block;width:52px;height:3px;background:#d22}
.play{left:115px;top:49px;width:60px;height:38px;background:#111}
.play::after{content:"";position:absolute;left:25px;top:11px;border-left:14px solid var(--white);border-top:8px solid transparent;border-bottom:8px solid transparent}
.video-label{left:641px;top:683px;width:166px;height:26px;background:var(--green);color:var(--white);font-family:"Rokkitt",Georgia,serif;font-weight:700;font-size:19px;padding:0 0 0 12px;line-height:26px}
.video-fold{left:641px;top:709px;border-top:6px solid var(--green-dark);border-left:14px solid transparent}

.portfolio{left:0;top:913px;width:1066px;height:204px;background:var(--grey-bg)}
.portfolio-title{left:108px;top:20px;font-family:"Sorts Mill Goudy",Georgia,serif;font-style:italic;font-size:26px;color:var(--heading)}
.pager{left:911px;top:34px;display:flex;gap:5px}
.pager i{width:12px;height:12px;border-radius:50%;background:#8c8c8c}
.pager i.on{background:var(--green)}
.arrow{top:71px;width:18px;height:94px;background:var(--green)}
.arrow::after{content:"";position:absolute;top:42px;left:5px;width:6px;height:6px;border:solid var(--white);border-width:0 2px 2px 0}
.arrow.prev::after{transform:rotate(135deg);left:7px}
.arrow.next::after{transform:rotate(-45deg);left:4px}
.thumb{top:71px;width:193px;height:94px}
.thumb.active{outline:3px solid var(--green);outline-offset:-3px}

.footer{left:0;top:1117px;width:1066px;height:83px;background:var(--dark);color:var(--white)}
.footer-links{left:110px;top:20px;display:flex;gap:12px;font-size:12px}
.footer-links span.sep{color:#bbb}
.copyright{left:110px;top:47px;font-size:12.5px;color:#cfcfcf}
.social{top:26px;width:36px;height:30px}
</style>
</head>
<body>

<div class="abs top-bar">
  <span style="left:663px">Call Now: 555.014.2300</span>
  <span style="left:812px">Who We Are</span>
  <span class="divider">|</span>
  <span style="left:907px">Contact Us</span>
</div>

<header class="abs header">
  <div class="abs brand"><span class="brand-dot"></span><span class="brand-name">Thistlewood Joinery</span></div>
  <nav class="abs nav">
    <a class="active">HOME</a>
    <a>GETTING STARTED</a>
    <a>CUSTOMER EXPERIENCE</a>
    <a>PROFESSIONAL</a>
    <a>PORTFOLIO</a>
    <a>CABINET HARDWARE</a>
  </nav>
</header>

<section class="abs hero">
  <svg class="abs hero-photo" width="873" height="318" viewBox="0 0 873 318" role="img" aria-label="Bright white kitchen with cabinets, range, windows and sunflowers">
    <defs>
      <linearGradient id="kitchenTone" x1="0" y1="0" x2="1" y2="1">
        <stop offset="0" stop-color="#d8c7ae"/>
        <stop offset=".5" stop-color="#ece8e0"/>
        <stop offset="1" stop-color="#a9b99a"/>
      </linearGradient>
    </defs>
    <path d="M0 0H873A458 458 0 0 1 0 0Z" fill="url(#kitchenTone)"/>
  </svg>
  <h1 class="abs hero-title">Stylish Kitchen Cabinets</h1>
  <p class="abs hero-sub">Lorem Ipsum is simply dummy text of the printing and typesetting industry. Lorem Ipsum<br>has been the industry's standard dummy text ever since the 1500s</p>
</section>
<div class="abs hero-band"></div>

<svg class="abs room-icon" style="left:333px" viewBox="0 0 76 86" aria-label="Kitchen">
  <polygon points="38,2 73,22 73,64 38,84 3,64 3,22" fill="#2a8a2a" transform="translate(0,2)"/>
  <polygon points="38,2 73,22 73,64 38,84 3,64 3,22" fill="var(--green)"/>
  <g stroke="#fff" stroke-width="5" stroke-linecap="round"><line x1="24" y1="58" x2="50" y2="28"/><line x1="26" y1="28" x2="52" y2="58"/></g>
</svg>
<svg class="abs room-icon" style="left:438px" viewBox="0 0 76 86" aria-label="Bathroom">
  <polygon points="38,2 73,22 73,64 38,84 3,64 3,22" fill="#fff" stroke="#ddd"/>
  <path d="M20 44h36v6a9 9 0 0 1-9 9H29a9 9 0 0 1-9-9z" fill="var(--icon)"/>
  <path d="M24 44V30a5 5 0 0 1 10 0" fill="none" stroke="var(--icon)" stroke-width="3"/>
</svg>
<svg class="abs room-icon" style="left:544px" viewBox="0 0 76 86" aria-label="Bedroom">
  <polygon points="38,2 73,22 73,64 38,84 3,64 3,22" fill="#fff" stroke="#ddd"/>
  <rect x="18" y="33" width="4" height="24" fill="var(--icon)"/>
  <rect x="22" y="38" width="9" height="7" rx="2" fill="var(--icon)"/>
  <rect x="22" y="45" width="36" height="7" fill="var(--icon)"/>
  <rect x="32" y="38" width="26" height="7" rx="2" fill="var(--icon)"/>
  <rect x="54" y="52" width="4" height="5" fill="var(--icon)"/>
</svg>
<svg class="abs room-icon" style="left:648px" viewBox="0 0 76 86" aria-label="Entertainment">
  <polygon points="38,2 73,22 73,64 38,84 3,64 3,22" fill="#fff" stroke="#ddd"/>
  <circle cx="38" cy="44" r="19" fill="var(--icon)"/>
  <circle cx="38" cy="44" r="6" fill="#fff"/>
  <circle cx="38" cy="44" r="2" fill="var(--icon)"/>
</svg>

<h2 class="abs about-title">Who We Are</h2>
<p class="abs about-text">Established in 1966, Thistlewood Joinery has long stood as one of the Midwest's most renowned makers of custom cabinets and fixtures. Our handcrafted, award-winning creations have been chosen by hundreds of noteworthy homebuilders. And while we custom build cabinets, we built our business around the belief that our customers absolutely, unequivocally come first. From day one, our mission has been to help turn the houses that people live in to the homes they've always dreamed of.</p>

<div class="abs video-card">
  <div class="abs video-screen" role="img" aria-label="Video still of a kitchen with wall oven and white cabinets">
    <div class="abs play"></div>
    <div class="abs video-controls"><div class="abs video-progress"><i></i></div></div>
  </div>
</div>
<div class="abs video-fold"></div>
<div class="abs video-label">Featured Video</div>

<section class="abs portfolio">
  <h2 class="abs portfolio-title">Portfolio</h2>
  <div class="abs pager"><i class="on"></i><i></i><i></i></div>
  <div class="abs arrow prev" style="left:107px"></div>
  <div class="abs thumb" style="left:132px;background:linear-gradient(100deg,#55514c,#b9b3aa 50%,#e6e1d8 75%,#6b4c33)" role="img" aria-label="Kitchen with stainless wall oven and white cabinetry"></div>
  <div class="abs thumb active" style="left:335px;background:linear-gradient(100deg,#2a221d,#4a3a30 50%,#7b5a40 80%,#2a221d)" role="img" aria-label="Dark wood kitchen island">
    <svg class="abs" style="left:88px;top:32px" width="30" height="30" viewBox="0 0 30 30"><circle cx="11" cy="11" r="7" fill="none" stroke="#fff" stroke-width="3"/><line x1="16" y1="16" x2="25" y2="25" stroke="#fff" stroke-width="4" stroke-linecap="round"/></svg>
  </div>
  <div class="abs thumb" style="left:536px;background:linear-gradient(100deg,#c9c6c2,#ebe8e2 45%,#a59684 80%,#5a4a3c)" role="img" aria-label="White kitchen with refrigerator and island"></div>
  <div class="abs thumb" style="left:738px;background:linear-gradient(100deg,#3d3027,#8c7a66 40%,#e5e0d6 70%,#cfc8bb)" role="img" aria-label="Kitchen with pendant lights and white cabinets"></div>
  <div class="abs arrow next" style="left:940px"></div>
</section>

<footer class="abs footer">
  <div class="abs footer-links">
    <span>ADVICE</span><span class="sep">|</span><span>ABOUT</span><span class="sep">|</span><span>CONTACT</span><span class="sep">|</span><span>PRIVACY POLICY</span><span class="sep">|</span><span>TERMS &amp; CONDITION</span>
  </div>
  <p class="abs copyright">copyright© 2014 Thistlewood. All Rights Reserved.</p>
  <div class="abs social" style="left:794px;background:#3b5998"></div>
  <div class="abs social" style="left:836px;background:#6a6a6a"></div>
  <div class="abs social" style="left:877px;background:#6a6a6a"></div>
  <div class="abs social" style="left:918px;background:#6a6a6a"></div>
</footer>

</body>
</html>
```